Web Design Project

This as the foundation http://lunorbix.com/demo_viewer/index.php?theme=velquistwp

Site needs to have a glossy black background with white text…..Extremely modern with a few flares of ravelle 6 style but nothing too off the wall, easily understood.

Here are some other reference sites and likes and dislikes that will help: (Probably overkill but we are looking for a cutting edge New York / LA Style )

http://www.torvikandcolb.com

Like- The black background with white font is very eye catching and clean. Love the contrast. Black is a great background for photographs and videos

http://samuelvorne.com

Like- Clean homepage, black and white color scheme works well.

http://douglaswhitcanephotography.com

Like- Nice Menu, nice B and W contrast

http://www.qkv.com

Like- Like the Menu. Clean and easy.

http://www.saffelmont.com

Like- Contrast of white background with black font.

Like- Slide show of stills (but should be able to click images to go to video. We’d also like the name of the project)

Like- Drop down menu allows for customer to find service they need without going through all services.

Like- Tells you work that they do right next to the logo.

Dislike- Too much information on homepage. Too much scrolling.

http://www.corbelvanestudios.com

Like- High Res images on home page

Like - The About Me is on homepage and speaks to potential customer directly. “We create award-winning videos for companies like yours.”

Like- Blog is updated with new projects they do. And short, visual entries

Like- “Work” section stands out from website. The background fades to light grey and white when you click on “work” so that the portfolio stands out more. Makes color look more vivid

Like- Black and white color scheme with grey header

http://www.fennwick748.com

Like- High Res images on home page pointing to projects

Like- Photograph as background, changes with different links. So work is always showcased and creates contrast. Information is laid over a barely translucent background, which is laid over the picture.

Like- They have a good Attitude about quality of their product

http://www.quillbramt.net

Like- First thing you see when open page is a clear big statement about what they do, said in a catchy way. They have a Tagline.

http://plimsworthdesign.com

Like- How work is categorized. Client list has links, which take you to their Client page with all their work grouped together. Nice flow and organization shows client relationships. And nice descriptions of what the job was and how it was executed… Way too wordy at times though

http://www.marivantphotography.com

Like- The homepage is very clean and accessible. Love the color scheme and how Logo is centered between the links.

Of the four designs we have gotten EVERY SINGLE ONE has been a template STOLEN from another site. We are paying for ORIGINAL design. Not copies and templates. Please ONLY submit original designs

```html
<!DOCTYPE html>
<html lang="en">
<head>
<meta charset="utf-8">
<title>Velmora Productions</title>
<link href="https://fonts.googleapis.com/css2?family=Titillium+Web:wght@400;600;700;900&display=swap" rel="stylesheet">
<style>
:root{
  --black:#050505;
  --header:#0b0b0b;
  --footer:#121212;
  --white:#ffffff;
  --muted:#9a9a9a;
  --field:#1f1f1f;
  --magenta:#a8085f;
  --violet:#7f00ff;
  --sky:#00a3e3;
  --teal:#1796bd;
  --plum:#6b2463;
  --stone:#d3cec6;
  --taupe:#7b6b5e;
  --gold:#ffc000;
  --crimson:#a5130f;
  --caption:#2b2a28;
}
*{margin:0;padding:0;box-sizing:border-box}
html,body{width:1200px;height:1120px;overflow:hidden;background:var(--black)}
body{position:relative;font-family:"Titillium Web",sans-serif;color:var(--white)}
.abs{position:absolute}
.site-header{left:0;top:0;width:1200px;height:107px;background:var(--header)}
.rule{left:0;width:1200px;height:5px;background:var(--white)}
.brand-box{left:196px;top:0;width:145px;height:130px;background:#000;display:flex;flex-direction:column;align-items:center;justify-content:center;z-index:3}
.brand-name{font-size:17px;font-weight:600;line-height:1.1;text-align:center;color:var(--white)}
.main-nav{left:410px;top:46px;display:flex;align-items:center;font-size:12.5px;font-weight:600;text-transform:uppercase;letter-spacing:.2px}
.main-nav a{color:var(--white);text-decoration:none;padding:0 8px;border-left:1px solid #444;line-height:13px}
.main-nav a:first-child{border-left:none;padding-left:0}
.nav-toggle{margin-left:14px}
.hero{left:0;top:115px;width:1200px;height:368px;background:linear-gradient(100deg,#4a4f57 0%,#6d6a69 30%,#b9b9b8 50%,#4d4b50 70%,#6f6a63 100%)}
.hero-controls{left:0;top:115px}
.section-title{left:198px;top:508px;font-size:24px;font-weight:600;text-transform:uppercase;letter-spacing:-.3px}
.tile{display:flex;align-items:center;justify-content:center;font-weight:900;color:var(--white);font-size:40px;letter-spacing:-1px}
.tile-caption{left:0;bottom:0;width:100%;height:41px;background:var(--caption);padding:4px 7px;font-size:11.5px;line-height:15px}
.tile-caption strong{display:block;font-weight:700}
.load-more{left:554px;top:833px;display:flex;align-items:center;gap:3px;font-size:11px;font-weight:900}
.load-icon{width:27px;height:27px;background:var(--white);display:flex;align-items:center;justify-content:center}
.site-footer{left:0;top:878px;width:1200px;height:242px;background:var(--footer)}
.footer-col h3{font-size:19px;font-weight:400;margin-bottom:4px;line-height:26px}
.footer-col ul{list-style:none;font-size:12.5px;line-height:17px;color:var(--muted)}
.field{width:178px;height:30px;background:var(--field);border-radius:2px;font-size:8.5px;color:#666;padding:9px 19px;margin-bottom:5px}
.submit{margin-top:1px;width:89px;height:30px;background:var(--magenta);font-size:12px;font-weight:600;text-transform:uppercase;display:flex;align-items:center;justify-content:center;border-radius:2px}
.social{display:flex;gap:6px;font-size:8px;color:var(--muted)}
.social span{display:flex;align-items:center;gap:2px}
.social i{display:inline-block;width:9px;height:9px;border:1px solid var(--white);border-radius:50%}
.footer-brand{left:870px;top:1000px;width:125px;font-size:17px;font-weight:600;text-align:center}
.footer-rule{left:0;top:1086px;width:1200px;height:1px;background:#262626}
.legal{left:0;top:1091px;width:1200px;text-align:center;font-size:9px;line-height:11px;color:#8a8a8a}
</style>
</head>
<body>
<header class="site-header abs"></header>
<div class="brand-box abs"><div class="brand-name">Velmora<br>Productions</div></div>
<nav class="main-nav abs">
  <a href="#">Show Reel</a><a href="#">Home</a><a href="#">Services</a><a href="#">Video Gallery</a><a href="#">About Us</a><a href="#">Actor Demo Reel</a><a href="#">Contact</a>
  <svg class="nav-toggle" width="13" height="13" viewBox="0 0 13 13"><circle cx="6.5" cy="6.5" r="6.5" fill="#fff"/><path d="M3.5 5h6l-3 3.5z" fill="#000"/></svg>
</nav>
<div class="rule abs" style="top:107px"></div>

<div class="hero abs" role="img" aria-label="Street film shoot with crew members gathered around a vintage black car"></div>
<svg class="hero-controls abs" width="1200" height="368" viewBox="0 0 1200 368">
  <g fill="none" stroke="#fff" stroke-width="2.5">
    <circle cx="238" cy="179" r="14"/><path d="M246 179h-15M237 172l-7 7 7 7"/>
    <circle cx="961" cy="179" r="14"/><path d="M953 179h15M962 172l7 7-7 7"/>
    <circle cx="590" cy="167" r="43" stroke-width="4"/>
  </g>
  <path d="M578 145v44l34-22z" fill="#fff"/>
  <g fill="#fff"><circle cx="576" cy="349" r="4"/><circle cx="588" cy="349" r="4"/><circle cx="600" cy="349" r="4"/><circle cx="612" cy="349" r="4"/><circle cx="624" cy="349" r="4"/></g>
</svg>
<div class="rule abs" style="top:485px"></div>

<h2 class="section-title abs">Our Projects</h2>
<div class="tile abs" style="left:196px;top:555px;width:198px;height:122px;background:var(--violet);font-size:46px">KDV</div>
<div class="tile abs" style="left:398px;top:555px;width:200px;height:122px;background:var(--sky);font-size:30px">Orla</div>
<div class="tile abs" style="left:603px;top:555px;width:195px;height:122px;background:var(--teal);font-size:30px">Pivo</div>
<div class="tile abs" style="left:802px;top:555px;width:193px;height:122px;background:var(--plum);font-size:30px">Nexa</div>
<div class="tile abs" style="left:196px;top:682px;width:198px;height:124px;background:var(--stone);align-items:flex-start;padding-top:16px">OSK
  <div class="tile-caption abs"><strong>OSK TABLET</strong>App</div></div>
<div class="tile abs" style="left:398px;top:682px;width:200px;height:124px;background:var(--taupe);font-size:30px">Bram</div>
<div class="tile abs" style="left:603px;top:682px;width:195px;height:124px;background:var(--gold)">Luma</div>
<div class="tile abs" style="left:802px;top:682px;width:193px;height:124px;background:var(--crimson)">Pelo</div>

<div class="load-more abs">
  <div class="load-icon"><svg width="18" height="10" viewBox="0 0 18 10"><path d="M1 1l8 7 8-7" fill="none" stroke="#000" stroke-width="2.5"/></svg></div>
  <span>LOAD MORE</span>
</div>

<footer class="site-footer abs"></footer>
<div class="footer-col abs" style="left:197px;top:893px"><h3>About us</h3>
  <ul><li>Home</li><li>About</li><li>Services</li><li>Projects</li><li>Community</li><li>Venture</li><li>Social</li><li>Contact</li></ul></div>
<div class="footer-col abs" style="left:388px;top:893px"><h3>Links</h3>
  <ul><li>Advertising</li><li>Branding</li><li>E-Commerce</li><li>Marketing</li><li>Mobile Apps</li><li>Social Media</li><li>Video</li><li>Web Design</li></ul></div>
<div class="footer-col abs" style="left:576px;top:893px"><h3>Contact Us Now</h3>
  <div class="field" style="margin-top:5px">Ful Name</div>
  <div class="field">Email</div>
  <div class="field">Phone Number</div>
  <div class="submit">Submit Now</div></div>
<div class="footer-col abs" style="left:880px;top:893px"><h3>Follow Us</h3>
  <div class="social" style="margin-top:5px"><span><i></i>Netlo</span><span><i></i>Chirpa</span><span><i></i>Bookly</span><span><i></i>Feed</span></div></div>
<div class="footer-brand abs">Velmora<br>Productions</div>

<div class="footer-rule abs"></div>
<div class="legal abs">Copyright © 2011 Kestrin Productions All rights reserved.<br>Developed By: ABCDEFG</div>
</body>
</html>
```